Talvon Crest Real estate in need of Logo design

I just started a new real estate brokerage company and need a professional, new logo design that I can incorporate through all forms of marketing and branding. I would like the business card to use both Matte finish and high gloss.

```html
<!DOCTYPE html>
<html lang="en">
<head>
<meta charset="UTF-8">
<title>Talvon Crest Real Estate – Business Cards</title>
<link href="https://fonts.googleapis.com/css2?family=Montserrat:wght@500;600;700&family=Roboto:wght@400&display=swap" rel="stylesheet">
<style>
  :root {
    --backdrop: #2b2b2d;
    --card: #0c0c0d;
    --silver: #d4d4d6;
    --silver-dim: #a9a9ac;
    --rule: #8a8a8e;
  }
  * { margin: 0; padding: 0; box-sizing: border-box; }
  html, body {
    width: 1200px; height: 1200px; overflow: hidden;
    background: var(--backdrop);
  }
  .sheet {
    width: 1200px; height: 1200px;
    display: flex; flex-direction: column; align-items: center; justify-content: center;
    gap: 56px;
  }
  .card {
    position: relative;
    width: 860px; height: 490px;
    background: var(--card);
    box-shadow: 0 18px 40px rgba(0,0,0,.55);
    color: var(--silver);
    font-family: 'Roboto', sans-serif;
  }
  .brand {
    display: flex; align-items: center; gap: 14px;
    font-family: 'Montserrat', sans-serif;
    font-weight: 600;
    color: var(--silver);
    letter-spacing: 1px;
    white-space: nowrap;
  }
  .brand-mark {
    width: 16px; height: 16px; background: var(--silver);
  }
  /* front */
  .card--front .brand {
    position: absolute; left: 50%; top: 200px; transform: translateX(-50%);
    font-size: 36px;
  }
  .card--front .web {
    position: absolute; left: 0; right: 0; top: 300px;
    text-align: center; font-size: 17px; color: var(--silver-dim); letter-spacing: .5px;
  }
  /* back */
  .holder { position: absolute; left: 70px; top: 70px; }
  .holder-name {
    font-family: 'Montserrat', sans-serif; font-weight: 700;
    font-size: 24px; letter-spacing: 1.5px; text-transform: uppercase;
  }
  .holder-role {
    margin-top: 4px; font-size: 17px; letter-spacing: 1px;
    text-transform: uppercase; color: var(--silver-dim);
  }
  .card--back .brand {
    position: absolute; right: 70px; top: 220px; font-size: 32px;
  }
  .divider {
    position: absolute; left: 70px; right: 70px; top: 312px;
    height: 1px; background: var(--rule);
  }
  .contacts {
    position: absolute; left: 70px; top: 340px;
    list-style: none; font-size: 19px; line-height: 34px;
  }
  .contacts li { display: flex; align-items: center; gap: 14px; }
  .contacts svg { width: 18px; height: 18px; fill: none; stroke: var(--silver); stroke-width: 1.6; }
  .address {
    position: absolute; right: 70px; top: 344px;
    display: flex; align-items: center; gap: 18px;
    font-size: 20px; line-height: 30px; text-align: right;
  }
  .address svg { width: 20px; height: 28px; fill: none; stroke: var(--silver); stroke-width: 1.6; }
</style>
</head>
<body>
<main class="sheet">
  <section class="card card--front">
    <div class="brand"><span class="brand-mark"></span>TALVON CREST REAL ESTATE</div>
    <p class="web">www.talvoncrest.com</p>
  </section>

  <section class="card card--back">
    <div class="holder">
      <p class="holder-name">Marcus Ellery</p>
      <p class="holder-role">Real Estate Broker</p>
    </div>
    <div class="brand"><span class="brand-mark"></span>TALVON CREST REAL ESTATE</div>
    <div class="divider"></div>
    <ul class="contacts">
      <li><svg viewBox="0 0 24 24"><path d="M5 3h4l2 5-3 2a12 12 0 0 0 6 6l2-3 5 2v4a2 2 0 0 1-2 2A17 17 0 0 1 3 5a2 2 0 0 1 2-2z"/></svg>2480-5512-7390</li>
      <li><svg viewBox="0 0 24 24"><rect x="3" y="5" width="18" height="14"/><path d="M3 5l9 8 9-8"/></svg>info@talvoncrest.com</li>
      <li><svg viewBox="0 0 24 24"><circle cx="12" cy="12" r="9"/><path d="M3 12h18M12 3c3 3 3 15 0 18M12 3c-3 3-3 15 0 18"/></svg>www.talvoncrest.com</li>
    </ul>
    <div class="address">
      <p>2871 Harbor Mill Road<br>Ocala, Florida 34471</p>
      <svg viewBox="0 0 20 28"><path d="M10 27S2 16 2 10a8 8 0 0 1 16 0c0 6-8 17-8 17z"/><circle cx="10" cy="10" r="3"/></svg>
    </div>
  </section>
</main>
</body>
</html>
```